Ridgeline Outfitters Business Cards

Recently had a logo done with Artfolio and now looking for a business card to go along with it.

Target Market(s)

Ridgeline Outfitters is a weapons dealer. My market will be primarily men, hunting, shooting type.

Industry/Entity Type

Business

Contact Information for Business Card

I selected double sided, but this is not required, single or double is going to be fine. I picture the logo on one side, or perhaps just the circle which contains "RO" with the remaining info on the other side.

Font styles to use
Sans Serif

Requirements
Must have
• My name: Milo Brandt
• Title: Owner
• tel: 612-555-0187
• web: www.ridgelineoutfittersmn.example
Nice to have
• I like the concept of a black business card. I would like to keep the colors monotone, black, grey, white or red. Red is acceptable because it is in the logo. I have also seen cards that are matte black with shiny black as well, perhaps for the logo (or circle RO) part of the logo.
• I will upload a couple of the logos for use, and also an example I just found of the black on black. and some others that have a nice contrast.
Should not have
• lots of colors are not wanted.

```html
<!DOCTYPE html>
<html lang="en">
<head>
<meta charset="utf-8">
<title>Ridgeline Outfitters – Business Card</title>
<link rel="stylesheet" href="https://fonts.googleapis.com/css2?family=Open+Sans:wght@300;400;600;700&display=swap">
<style>
  :root {
    --backdrop: #e9e6e1;
    --card: #2a2930;
    --red: #d3303a;
    --red-deep: #b8262f;
    --white: #f4f4f4;
    --grey: #8d8c92;
  }
  * { margin: 0; padding: 0; box-sizing: border-box; }
  html, body {
    width: 1200px;
    height: 799px;
    overflow: hidden;
    background: var(--backdrop);
    font-family: "Open Sans", sans-serif;
  }
  .card {
    position: absolute;
    left: 180px;
    top: 160px;
    width: 840px;
    height: 480px;
    background: var(--card);
    border-radius: 6px;
    box-shadow: 0 14px 40px rgba(0,0,0,0.25);
    overflow: hidden;
  }
  .card__stripes {
    position: absolute;
    inset: 0;
  }
  .brand {
    position: absolute;
    right: 54px;
    top: 58px;
    display: flex;
    align-items: center;
    gap: 14px;
  }
  .brand__circle {
    width: 46px;
    height: 46px;
    border-radius: 50%;
    border: 4px solid var(--grey);
  }
  .brand__name {
    font-weight: 700;
    font-size: 22px;
    letter-spacing: 0.06em;
    text-transform: uppercase;
    color: var(--red);
  }
  .person {
    position: absolute;
    left: 62px;
    top: 172px;
    color: var(--white);
  }
  .person__name {
    font-weight: 300;
    font-size: 52px;
    letter-spacing: 0.01em;
    line-height: 1.1;
  }
  .person__details {
    list-style: none;
    margin-top: 10px;
    font-size: 16px;
    font-weight: 400;
    line-height: 1.45;
  }
  .website {
    position: absolute;
    left: 62px;
    bottom: 66px;
    color: var(--white);
    font-size: 17px;
    font-weight: 600;
    letter-spacing: 0.01em;
  }
</style>
</head>
<body>
  <div class="card">
    <svg class="card__stripes" width="840" height="480" viewBox="0 0 840 480" aria-hidden="true">
      <rect x="0" y="132" width="840" height="9" fill="var(--red)"/>
      <polygon points="560,141 840,141 840,196 590,196" fill="var(--red)"/>
    </svg>

    <div class="brand">
      <span class="brand__circle"></span>
      <span class="brand__name">Ridgeline Outfitters</span>
    </div>

    <div class="person">
      <h1 class="person__name">Milo Brandt</h1>
      <ul class="person__details">
        <li>// Owner</li>
        <li>// 612-555-0187</li>
      </ul>
    </div>

    <p class="website">www.ridgelineoutfittersmn.example</p>
  </div>
</body>
</html>
```